Toronto based company needs a logo and business card design

We are "Bellmora Restoration Corp.". A high rise building restoration company based in Toronto. We specialize in Building Envelope, Parking Garage and Waterproofing repairs. Would like to see designs which use the color Teal, Black and White or Red, Black and White. Prefer to have light color background for the front of the card and dark background for the reverse side. For logo design, we would prefer to see high rise building/s incorporated in it.

Industry/Entity Type

Construction

Logo Text

Bellmora

Font styles to use
Sans Serif

Colors
00a990
ffffff
ec1f27
85acd3
000000

```html
<!DOCTYPE html>
<html lang="en">
<head>
<meta charset="utf-8">
<title>Bellmora Restoration Corp. – Business Card</title>
<link rel="stylesheet" href="https://fonts.googleapis.com/css2?family=Lato:wght@400;700&display=swap">
<style>
  :root {
    --red: #ec1f27;
    --black: #161616;
    --white: #ffffff;
    --ink: #333333;
    --grey-text: #6b6b6b;
    --stage: #7a7a7a;
  }
  * { box-sizing: border-box; margin: 0; padding: 0; }
  html, body { width: 1200px; height: 802px; overflow: hidden; }
  body {
    position: relative;
    background: var(--stage);
    font-family: "Lato", Arial, sans-serif;
  }
  .card {
    position: absolute;
    top: 274px;
    width: 443px;
    height: 264px;
    overflow: hidden;
    box-shadow: 0 3px 6px rgba(0,0,0,0.35);
  }
  .card-front { left: 136px; background: var(--white); }
  .card-back { left: 624px; background: var(--black); }
  .card-band {
    position: absolute;
    left: 0; right: 0; bottom: 0;
    height: 7px;
    background: var(--red);
  }

  /* front */
  .front-accent { position: absolute; left: 0; top: 0; }
  .company-name {
    position: absolute;
    left: 25px; top: 44px;
    width: 200px;
    color: var(--red);
    font-weight: 700;
    font-size: 19px;
    line-height: 22px;
    letter-spacing: 0.3px;
    text-transform: uppercase;
  }
  .person-name {
    position: absolute;
    left: 25px; top: 113px;
    color: var(--red);
    font-weight: 700;
    font-size: 16px;
    letter-spacing: 0.3px;
    text-transform: uppercase;
  }
  .person-title {
    position: absolute;
    left: 25px; top: 131px;
    color: var(--ink);
    font-size: 12.5px;
  }
  .contact-list {
    position: absolute;
    left: 25px; top: 148px;
    list-style: none;
    color: var(--ink);
    font-size: 12.5px;
    line-height: 16px;
  }
  .contact-list li { display: flex; align-items: center; gap: 4px; }
  .contact-list svg { width: 10px; height: 10px; fill: var(--red); flex: none; }
  .address {
    position: absolute;
    left: 25px; top: 218px;
    color: var(--ink);
    font-size: 12.5px;
    line-height: 16px;
  }

  /* back */
  .back-accent { position: absolute; left: 0; top: 0; }
  .back-rule {
    position: absolute;
    left: 108px;
    width: 228px;
    height: 2px;
    background: var(--red);
  }
  .back-rule.top { top: 142px; }
  .back-rule.bottom { top: 210px; }
  .back-name {
    position: absolute;
    left: 0; right: 0; top: 148px;
    text-align: center;
    color: var(--red);
    font-weight: 700;
    font-size: 29px;
    line-height: 30px;
    text-transform: uppercase;
    letter-spacing: 0.5px;
  }
  .back-name span { display: block; font-size: 17px; line-height: 26px; letter-spacing: 1px; }
</style>
</head>
<body>
  <section class="card card-front">
    <svg class="front-accent" width="443" height="264" viewBox="0 0 443 264" aria-hidden="true">
      <circle cx="390" cy="170" r="125" fill="var(--red)"/>
    </svg>
    <h1 class="company-name">Bellmora Restoration Corp.</h1>
    <h2 class="person-name">Dorian Keller</h2>
    <p class="person-title">Managing Director</p>
    <ul class="contact-list">
      <li><svg viewBox="0 0 10 10"><path d="M1 3c0-1.5 8-1.5 8 0v1H7V3H3v1H1zM2 5h6l1 4H1z"/></svg>044-555 010 220</li>
      <li><svg viewBox="0 0 10 10"><path d="M2.5 0h5v10h-5zM3.5 1v7h3V1z"/></svg>044-555 010 220</li>
      <li><svg viewBox="0 0 10 10"><path d="M0 2h10v6H0zM1 3l4 3 4-3z" fill-rule="evenodd"/></svg>info@bellmora-example.com</li>
      <li><svg viewBox="0 0 10 10"><circle cx="5" cy="5" r="4.5"/></svg>www.bellmora-example.com</li>
    </ul>
    <p class="address">4820, Harbour Row Suite 12<br>Toronto, Canada, M5V 2T6.</p>
    <div class="card-band"></div>
  </section>

  <section class="card card-back">
    <svg class="back-accent" width="443" height="264" viewBox="0 0 443 264" aria-hidden="true">
      <circle cx="221" cy="104" r="26" fill="var(--red)"/>
    </svg>
    <div class="back-rule top"></div>
    <p class="back-name">Bellmora<span>Restoration Corp.</span></p>
    <div class="back-rule bottom"></div>
    <div class="card-band"></div>
  </section>
</body>
</html>
```